Website Performance Testing eBook for the software testing industry

Overview:
I would like an ebook/whitepaper designed. This ebook will be digital published on my website as a lead generation piece. The purpose is to give high level tips on what to look for and things to think about when working on a website performance testing project.
The ebook also demonstrates our expertise and knowledge on the topic.
Topic:
This is an ebook on software testing. Specifically, website performance testing.
About Brindlecove:
Brindlecove Solutions is an outsourcing development and software testing firm, and we provide expert services for application development, testing and data analytics. We extend our clients’ software testing capabilities with on-demand technical expertise. Our quality assurance resources work as part of our clients’ teams to help test applications on time and within budget.
Our model is designed to allocate the right mix of local and offshore resources in order to optimize expertise, speed and cost. We provide the ability to quickly add specialty skills to our client’s development team without them incurring long-term costs. The result is far better management of resource capacities and outcomes.
Background on our branding and previous pieces:
I have included a few of our previous ebooks and whitepapers. I like the look and feel of these pieces, however we have made updates to our brand guidelines since them, so the new brand guidelines will need to be incorporated, and I'd like to refresh/update what we have done in the past.
Refer to our website for an idea of our look and feel. This page is one of our newer sections and would be a good reference:
http://www.brindlecove.example/data-analytics/
Tone and feel:
- The look and feel should be professional, clean and polished.
- I like good use of whitespace.
- I would prefer to keep stock photography of people to a minimum. Any images should add to the content and be relevant to the content.
(Also, I uploaded some InDesign files in case you wanted to refer to those assets, but I didn't include the Links folder because they were too big. If there's anything you more you need, let me know)
Target Market(s)
Audience:
The audience is senior Quality Assurance and Software Testing professionals.
- 30-45 years old
- Technical mindset
- Interested in learning
Titles include
- QA Lead
- QA Manager
- QA Director
- Director or VP of Development
- QA Automation Engineer
Our customers are medium to large sized companies. Many are software companies, but many are also enterprises in all almost all industries.

```html
<!DOCTYPE html>
<html lang="en">
<head>
<meta charset="utf-8">
<title>Website Performance Testing – Brindlecove Solutions</title>
<link href="https://fonts.googleapis.com/css2?family=Open+Sans:wght@300;400;600;700;800&display=swap" rel="stylesheet">
<style>
  :root {
    --brand-red: #e03a33;
    --band-grey: #c3c6c6;
    --ink: #111111;
    --body-text: #5a5a5a;
    --subhead: #4d4d4d;
    --footer-text: #7a7a7a;
    --paper: #ffffff;
    --wash: #f1f1f1;
  }
  * { margin: 0; padding: 0; box-sizing: border-box; }
  html, body { width: 848px; height: 1200px; overflow: hidden; background: var(--paper); }
  .page {
    position: relative;
    width: 848px; height: 1200px;
    font-family: "Open Sans", Arial, sans-serif;
    background: linear-gradient(to bottom, var(--wash) 0, var(--paper) 110px, var(--paper) 1060px, var(--wash) 1180px);
    overflow: hidden;
  }
  .band { position: absolute; left: 0; width: 848px; height: 20px; background: var(--band-grey); }
  .band::after { content: ""; position: absolute; top: 0; left: 669px; right: 0; bottom: 0; background: var(--brand-red); }
  .band--top { top: 0; }
  .band--bottom { bottom: 0; }

  .brand-name {
    position: absolute; top: 36px; right: 13px;
    font-size: 26px; font-weight: 600; color: var(--brand-red);
    letter-spacing: -0.2px;
  }

  .page-title {
    position: absolute; left: 67px; top: 138px;
    font-size: 35px; font-weight: 700; color: var(--ink); letter-spacing: 0.2px;
  }
  .intro { position: absolute; left: 67px; top: 216px; width: 703px; }
  .copy {
    font-size: 19px; font-weight: 300; line-height: 24px; color: var(--body-text);
    text-align: justify; hyphens: manual;
  }
  .section-title {
    position: absolute; left: 58px; top: 399px;
    font-size: 27px; font-weight: 700; color: var(--ink);
  }
  .section-body { position: absolute; left: 58px; top: 470px; width: 704px; }
  .section-body .copy, .subsection-body { font-size: 20px; }
  .section-body .copy + .copy { margin-top: 24px; }
  .subsection-title {
    position: absolute; left: 58px; top: 865px;
    font-size: 27px; font-weight: 700; color: var(--subhead);
  }
  .subsection-body { position: absolute; left: 58px; top: 909px; width: 704px; }

  .footer-trail, .footer-page {
    position: absolute; top: 1154px; font-size: 15px; font-weight: 300; color: var(--footer-text);
  }
  .footer-trail { left: 58px; }
  .footer-page { right: 25px; }
</style>
</head>
<body>
<div class="page">
  <div class="band band--top"></div>
  <div class="brand-name">Brindlecove Solutions</div>

  <h1 class="page-title">WEBSITE PERFORMANCE TESTING</h1>
  <p class="intro copy">Like any software product, your website or web application requires thorough testing before it goes live to ensure a quality user experience. Web users are accustomed to a high level of functionality, responsiveness and usability. Increasingly, they lack patience for web sites that do not provide a fulfilling experience. Thus, testing the performance aspects of your website is critical</p>

  <h2 class="section-title">TYPES OF PERFORMANCE TESTING</h2>
  <div class="section-body">
    <p class="copy">Performance testing assesses your site's efficiency compared to its specifica&shy;tions. Its main focus is overall responsiveness under average loads. This catego&shy;ry of testing should be performed early and often in order to uncover imbalanc&shy;es in the software architecture or its implementation. Monopolization of resources, processing bottlenecks and unexpected latency are likely suspects, which are easier to correct early on rather than at later stages in development or testing.</p>
    <p class="copy">The end result of these performance tests and subsequent software changes is a set of baseline measurements you apply whenever the web site is changed to ensure that responsiveness and processing efficiency are stable and improving.</p>
    <p class="copy">Let us look at two specific types of website performance testing: Load Testing and Stress Testing.</p>
  </div>

  <h3 class="subsection-title">01. Load Testing</h3>
  <p class="subsection-body copy">After early performance test results stabilizes, load tests that simulate thou&shy;sands or even millions of users over long time periods are appropriate for mea&shy;suring software endurance and volume capacity. These take you one step closer to real-world conditions. These tests uncover buffer overflows, memory leaks, and responsiveness degradation.</p>

  <div class="footer-trail">Main Topic &nbsp;&gt; Main Subtopic &nbsp;&gt; Subtopic</div>
  <div class="footer-page">Page 01 of 103</div>
  <div class="band band--bottom"></div>
</div>
</body>
</html>
```